Tulven Electrics Flyer Design Advertising

I am after an A5 Flyer design to help promote my electrical services business.
I would like to have information on what my business offers, photos of electrical work, and specials/deals for an amount of time.

Industry/Entity Type

Electrician

Font styles to use
Sans Serif

Colors
0292cd
33a6d7
85cae6
3176b5
333333
1b1b1b
ffffff
5c5c5c
474747

Requirements
Must have
• Specialising in New homes, renovations and commercial projects
• Contact details:
• ph. 0437 619 458
• email admin@tulvenelectrics.example.au
• facebook TulvenElectrics
• Specials/Deals:
• 10% off all electrical services
• or
• Free LED downlights on installation
• *Terms conditions apply
• ALL RESIDENTIAL & COMMERCIAL ELECTRICAL SERVICES
• - New Home installations
• - Commercial projects
• - Shop fit outs
• - Renovations
• - Smoke Detectors
• - Air Conditioning and Ceiling Fans
• - Garden Lighting
• - Oven and Cooktop Installations
• - Power Point installation
• - LED lighting upgrades
• - Security Lighting
• - Switchboard upgrades
• - Test and Tag
• - Commercial Property
• - General Electrical Maintenance

```html
<!DOCTYPE html>
<html lang="en">
<head>
<meta charset="utf-8">
<title>Tulven Electrics Flyer</title>
<link href="https://fonts.googleapis.com/css2?family=Lato:wght@400;700;900&family=Saira+Semi+Condensed:wght@600;700&display=swap" rel="stylesheet">
<style>
  :root{
    --blue:#0292cd;
    --blue-mid:#33a6d7;
    --blue-light:#85cae6;
    --blue-deep:#3176b5;
    --ink:#333333;
    --ink-dark:#1b1b1b;
    --grey:#5c5c5c;
    --grey-dark:#474747;
    --white:#ffffff;
    --page:#f2e3e4;
  }
  *{box-sizing:border-box;margin:0;padding:0}
  html,body{width:1200px;height:1026px;overflow:hidden;background:var(--page)}
  body{font-family:"Lato",sans-serif;position:relative}
  .flyer{position:absolute;left:253px;top:23px;width:694px;height:980px;background:linear-gradient(180deg,#ffffff 50%,#eef1f4 100%);overflow:hidden;box-shadow:0 14px 40px rgba(0,0,0,.18)}
  .hero{position:absolute;left:0;top:0;width:694px;height:540px;display:block}
  .brand{position:absolute;left:38px;top:52px;display:flex;align-items:center;gap:12px}
  .brand-dot{width:46px;height:46px;border-radius:50%;background:var(--blue)}
  .brand-name{font-family:"Lato",sans-serif;font-weight:900;font-size:30px;color:var(--ink);line-height:1}
  .headline{position:absolute;left:0;width:100%;top:548px;text-align:center;font-family:"Saira Semi Condensed",sans-serif;font-weight:700;color:var(--ink);font-size:33px;line-height:40px;text-transform:uppercase}
  .headline .lead{color:var(--blue);text-transform:none}
  .services{position:absolute;left:44px;top:640px;width:606px;height:232px;background:var(--blue);border-radius:16px;box-shadow:0 4px 0 #cfd8df}
  .services-tab{position:absolute;left:22px;top:10px;right:22px;height:44px;background:var(--white);border-radius:22px 22px 22px 4px;display:flex;align-items:center;justify-content:center;font-weight:700;font-size:21px;color:var(--blue)}
  .service-list{position:absolute;top:70px;list-style:none;color:var(--white);font-weight:700;font-size:15.5px;line-height:19.5px}
  .service-list li{position:relative;padding-left:26px}
  .service-list li::before{content:"";position:absolute;left:2px;top:7px;width:6px;height:6px;border-radius:50%;background:var(--white)}
  .service-list.left{left:44px}
  .service-list.right{left:340px;width:200px}
  .specials{position:absolute;left:44px;top:880px;width:620px;height:56px}
  .specials-label{position:absolute;left:0;top:0;width:128px;height:56px;background:var(--ink);color:var(--white);font-weight:700;font-size:19px;line-height:22px;padding:6px 0 0 16px;clip-path:polygon(0 0,86% 0,100% 50%,86% 100%,0 100%)}
  .deal{position:absolute;top:-4px;text-align:left;color:var(--ink);font-size:16px}
  .deal strong{display:block;color:var(--blue);font-weight:900;font-size:38px;line-height:40px}
  .deal.one{left:146px}
  .deal.two{left:360px}
  .or{position:absolute;left:318px;top:10px;width:30px;height:30px;border-radius:50%;background:var(--blue);color:var(--white);font-size:14px;font-weight:700;display:flex;align-items:center;justify-content:center}
  .terms{position:absolute;left:590px;top:8px;font-size:7px;line-height:8px;color:var(--grey);width:34px}
  .contact-bar{position:absolute;left:0;bottom:0;width:100%;height:46px;background:var(--ink);display:flex;align-items:center;gap:22px;padding-left:36px;color:var(--white);font-weight:700;font-size:16px}
  .contact{display:flex;align-items:center;gap:8px}
  .contact svg{width:24px;height:24px}
  .social-dot{width:22px;height:22px;border-radius:50%;border:2px solid var(--white)}
</style>
</head>
<body>
<main class="flyer">
  <svg class="hero" viewBox="0 0 694 540" xmlns="http://www.w3.org/2000/svg">
    <defs>
      <linearGradient id="dusk" x1="0" y1="0" x2="0" y2="1">
        <stop offset="0" stop-color="#6c7fa8"/>
        <stop offset=".45" stop-color="#8c8a8f"/>
        <stop offset=".7" stop-color="#5d4a35"/>
        <stop offset="1" stop-color="#3e4a2a"/>
      </linearGradient>
      <linearGradient id="kitchen" x1="0" y1="0" x2="1" y2="1">
        <stop offset="0" stop-color="#f4f4f2"/>
        <stop offset="1" stop-color="#9aa39a"/>
      </linearGradient>
      <linearGradient id="dining" x1="0" y1="0" x2="0" y2="1">
        <stop offset="0" stop-color="#ece8e2"/>
        <stop offset="1" stop-color="#7c6a58"/>
      </linearGradient>
    </defs>
    <g role="img" aria-label="Photo of a modern home patio lit at dusk with palm trees">
      <rect x="0" y="0" width="694" height="500" fill="url(#dusk)"/>
    </g>
    <rect x="12" y="12" width="310" height="150" rx="26" fill="#ffffff" opacity=".9"/>
    <path d="M0 300 C40 380 90 430 200 470 L0 470 Z" fill="var(--blue-deep)"/>
    <path d="M0 400 C160 470 420 430 694 440 L694 470 C430 470 200 500 0 450 Z" fill="var(--blue-deep)"/>
    <path d="M0 430 C200 500 440 470 694 470 L694 540 L0 540 Z" fill="#ffffff"/>
    <path d="M200 470 C350 485 520 462 694 458" stroke="var(--blue)" stroke-width="5" fill="none"/>
    <g role="img" aria-label="Photo of a bright kitchen with pendant lights">
      <circle cx="150" cy="380" r="104" fill="url(#kitchen)" stroke="#ffffff" stroke-width="7"/>
    </g>
    <g role="img" aria-label="Photo of a kitchen island with bar stools">
      <circle cx="318" cy="462" r="76" fill="url(#dining)" stroke="#ffffff" stroke-width="7"/>
    </g>
  </svg>

  <div class="brand">
    <span class="brand-dot"></span>
    <span class="brand-name">Tulven Electrics</span>
  </div>

  <h1 class="headline"><span class="lead">Specialising In:</span> New Homes,<br>Renovations &amp; Commercial Projects</h1>

  <section class="services">
    <h2 class="services-tab">All Residential &amp; Commercial Electrical Services</h2>
    <ul class="service-list left">
      <li>New Home installations</li>
      <li>Commercial projects</li>
      <li>Shop fit outs</li>
      <li>Renovations</li>
      <li>Smoke Detectors</li>
      <li>Air Conditioning and Ceiling Fans</li>
      <li>Garden Lighting</li>
      <li>Oven and Cooktop Installations</li>
    </ul>
    <ul class="service-list right">
      <li>Power Point installation</li>
      <li>LED lighting upgrades</li>
      <li>Security Lighting</li>
      <li>Switchboard upgrades</li>
      <li>Test and Tag</li>
      <li>Commercial Property</li>
      <li>General Electrical Maintenance</li>
    </ul>
  </section>

  <section class="specials">
    <div class="specials-label">Specials<br>Deals:</div>
    <div class="deal one"><strong>10% off</strong>all electrical services</div>
    <div class="or">or</div>
    <div class="deal two"><strong>Free LED</strong>downlights on installation</div>
    <div class="terms">*Terms conditions apply</div>
  </section>

  <footer class="contact-bar">
    <span class="contact">
      <svg viewBox="0 0 24 24"><circle cx="12" cy="12" r="10.5" fill="none" stroke="#fff" stroke-width="1.6"/><path d="M8.5 6.5l2 2.5-1.2 1.4c.8 1.7 2.1 3 3.8 3.8l1.4-1.2 2.5 2-1.2 1.8c-4.5-.3-8.7-4.5-9-9z" fill="#fff"/></svg>
      0437 619 458
    </span>
    <span class="contact">
      <svg viewBox="0 0 24 24"><circle cx="12" cy="12" r="10.5" fill="none" stroke="#fff" stroke-width="1.6"/><rect x="6.5" y="8" width="11" height="8" fill="none" stroke="#fff" stroke-width="1.4"/><path d="M6.5 8l5.5 4.5L17.5 8" fill="none" stroke="#fff" stroke-width="1.4"/></svg>
      admin@tulvenelectrics.example.au
    </span>
    <span class="contact">
      <span class="social-dot"></span>
      TulvenElectrics
    </span>
  </footer>
</main>
</body>
</html>
```